Adapt logo for box truck wrap for my restoration company

I need a wrap for our company Brightway Restoration. We specialize in water damage restoration. I’ve attached our logo, business card, and page header. Things I would like to include are- 24 hour emergency service, our phone number (555)014-7392 and that we do water, fire and mold work. It’s a 2004 Kardella Vonter which I’ve attached pictures of. I will get the cab wrapped as well.

Industry/Entity Type

Construction- specifically Restoration

Font styles to use
Sans Serif

Colors

Designer to choose colors to be used in the design.

Requirements
Must have
• Water• Fire• Mold, phone number (555)014-7392
Nice to have
• Clean, professional look with the logo

```html
<!DOCTYPE html>
<html lang="en">
<head>
<meta charset="utf-8">
<title>Brightway Restoration – Box Truck Side Wrap</title>
<link rel="stylesheet" href="https://fonts.googleapis.com/css2?family=Lexend:wght@600;700&family=Montserrat:wght@700;800&display=swap">
<style>
  :root {
    --page: #e9edf1;
    --panel: #ffffff;
    --water: #00c8f8;
    --water-deep: #1a8fd6;
    --fire: #e8610f;
    --fire-core: #ffd21a;
    --mold: #9c9a8f;
    --mold-dark: #3b3d36;
    --brand-blue: #3d8bd3;
    --brand-grey: #7c7c7c;
    --alert-red: #e8131b;
    --white: #ffffff;
  }
  * { box-sizing: border-box; margin: 0; padding: 0; }
  html, body {
    width: 1200px;
    height: 866px;
    overflow: hidden;
    background: var(--page);
  }
  .wrap-panel {
    position: absolute;
    left: 20px;
    top: 168px;
    width: 1160px;
    height: 530px;
    background: var(--panel);
    box-shadow: 0 6px 24px rgba(0, 0, 0, 0.12);
  }
  .wrap-panel svg {
    display: block;
    width: 100%;
    height: 100%;
  }
  .service-title {
    font-family: "Lexend", sans-serif;
    font-weight: 700;
    font-size: 76px;
    fill: var(--white);
    text-anchor: middle;
  }
  .emergency-label {
    font-family: "Lexend", sans-serif;
    font-weight: 700;
    font-size: 37px;
    fill: var(--white);
    text-anchor: end;
  }
  .hours-label {
    font-family: "Montserrat", sans-serif;
    font-weight: 800;
    font-style: italic;
    font-size: 44px;
    fill: var(--alert-red);
    text-anchor: middle;
  }
  .phone-number {
    font-family: "Lexend", sans-serif;
    font-weight: 600;
    font-size: 80px;
    fill: var(--brand-blue);
  }
  .brand-name {
    font-family: "Lexend", sans-serif;
    font-weight: 700;
    font-size: 28px;
    fill: var(--brand-blue);
  }
</style>
</head>
<body>
  <div class="wrap-panel">
    <svg viewBox="0 0 1510 690" preserveAspectRatio="xMidYMid meet" xmlns="http://www.w3.org/2000/svg">
      <defs>
        <radialGradient id="water-tone" cx="45%" cy="40%" r="65%">
          <stop offset="0" stop-color="#d8f6ff"/>
          <stop offset="0.55" stop-color="#5cc8f2"/>
          <stop offset="1" stop-color="#1a8fd6"/>
        </radialGradient>
        <radialGradient id="fire-tone" cx="50%" cy="60%" r="65%">
          <stop offset="0" stop-color="#ffd21a"/>
          <stop offset="0.55" stop-color="#f28a14"/>
          <stop offset="1" stop-color="#d2310f"/>
        </radialGradient>
        <radialGradient id="mold-tone" cx="50%" cy="50%" r="65%">
          <stop offset="0" stop-color="#d9d9d4"/>
          <stop offset="0.6" stop-color="#6f726a"/>
          <stop offset="1" stop-color="#3b3d36"/>
        </radialGradient>
      </defs>

      <!-- service bands -->
      <polygon class="band band--water" points="190,0 520,0 340,330 60,330" fill="var(--water)"/>
      <polygon class="band band--fire" points="555,0 885,0 705,330 425,330" fill="var(--fire)"/>
      <polygon class="band band--mold" points="915,0 1245,0 1065,330 785,330" fill="var(--mold)"/>
      <path class="band band--brand" d="M1290,20 L1505,20 L1505,478 L1290,478 Q1255,410 1180,410 L1130,410 Z" fill="var(--brand-blue)"/>

      <!-- service titles -->
      <text class="service-title" x="320" y="105">WATER</text>
      <text class="service-title" x="685" y="105">FIRE</text>
      <text class="service-title" x="1050" y="105">MOLD</text>

      <!-- service illustrations -->
      <g role="img" aria-label="Illustration of a splashing water wave inside a circle">
        <circle cx="200" cy="360" r="150" fill="url(#water-tone)"/>
      </g>
      <g role="img" aria-label="Illustration of flames inside a circle">
        <circle cx="570" cy="365" r="150" fill="url(#fire-tone)"/>
      </g>
      <g role="img" aria-label="Illustration of a mold growth texture inside a circle">
        <circle cx="930" cy="370" r="150" fill="url(#mold-tone)"/>
      </g>

      <!-- emergency badge -->
      <path class="emergency-badge" d="M0,552 H290 V635 Q290,660 265,660 H0 Z" fill="var(--alert-red)"/>
      <text class="emergency-label" x="255" y="598">EMERGENCY</text>
      <text class="emergency-label" x="255" y="643">SERVICE</text>

      <!-- 24 hour icon -->
      <g class="hours-icon" stroke-linecap="round">
        <g stroke="var(--alert-red)" stroke-width="3">
          <line x1="395" y1="515" x2="395" y2="530"/>
          <line x1="395" y1="670" x2="395" y2="685"/>
          <line x1="310" y1="600" x2="325" y2="600"/>
          <line x1="465" y1="600" x2="480" y2="600"/>
          <line x1="335" y1="540" x2="345" y2="550"/>
          <line x1="445" y1="650" x2="455" y2="660"/>
          <line x1="335" y1="660" x2="345" y2="650"/>
          <line x1="455" y1="540" x2="445" y2="550"/>
        </g>
        <path d="M430,555 A55,55 0 1,0 450,600" fill="none" stroke="var(--brand-blue)" stroke-width="6"/>
        <path d="M395,545 Q420,540 432,552" fill="none" stroke="var(--brand-blue)" stroke-width="10"/>
        <polygon points="425,535 450,560 422,566" fill="var(--brand-blue)"/>
        <text class="hours-label" x="398" y="618">24h</text>
      </g>

      <!-- phone -->
      <text class="phone-number" x="497" y="626">(555)014-7392</text>

      <!-- brand -->
      <circle class="brand-mark" cx="1160" cy="575" r="78" fill="var(--brand-blue)"/>
      <text class="brand-name" x="1262" y="565">BRIGHTWAY</text>
      <text class="brand-name" x="1262" y="610" textLength="205" lengthAdjust="spacing">RESTORATION</text>
    </svg>
  </div>
</body>
</html>
```